Packaging sleeve for Kraft Box

I need an urgent sleeve made for my box. I have the logo , business name and slogan. I have all the nutritional values and ingredients.for you to get an idea.
Luxurious item with colours like gold, cream, browns I have included some colour ideas and pictures of my marshmallows
The box measures 125x125x75mm
The sleeve will be 55mm
we sell award winning gourmet marshmallows.
These are very light and delecate.
There are 4 flavours which will need to be included on the sleeve. The box is Kraft material
The font I would like you to use is "Milasian Circa for the 4 flavours which are.
Rosewater & Strawberry ( needs 2 star award logo placed by the name.)
Dark Chocolate & Vanilla (needs 1 star award placed by the name)
Chocolate Orange
Crispy Salted Caramel

Target Market(s)

Luxury adult both male and female

Industry/Entity Type

Food Store

Font styles to use
Script
Other font styles liked:
• Milasian Circa

Requirements
Must have
• Colours that work with the logo colours and Kraft Box.
• Logo, business name and slogan need to be in gold
• Elegant simple design
Nice to have
• Delicate decorative swirl pattern on parts of the sleeve
• Try and use some colours behind the flavour names to reflect the marshmallow flavours i.e rose colour for the rosewater and brown for chocolate, orange for the orange chocolate and so on.
Should not have
• Busy patterns or clip art.

```html
<!DOCTYPE html>
<html lang="en">
<head>
<meta charset="utf-8">
<title>Nell's Confections – Rosewater &amp; Strawberry Sleeve</title>
<link href="https://fonts.googleapis.com/css2?family=Kaushan+Script&family=Montserrat:wght@400&display=block" rel="stylesheet">
<style>
  :root {
    --stripe-dark: #1f1411;
    --stripe-brown: #5b3e22;
    --panel: #2a1613;
    --gold: #c9a447;
    --title-gold: #e9b83a;
    --cream: #efe4cf;
  }
  html, body {
    margin: 0;
    padding: 0;
    width: 1200px;
    height: 161px;
    overflow: hidden;
  }
  .sleeve {
    position: relative;
    width: 1200px;
    height: 161px;
    background: repeating-linear-gradient(
      -45deg,
      var(--stripe-dark) 0 9px,
      var(--stripe-brown) 9px 14px
    );
  }
  .panel {
    position: absolute;
    top: 17px;
    height: 130px;
    background: var(--panel);
    border: 1px solid var(--gold);
    box-sizing: border-box;
    overflow: hidden;
  }
  .panel--back   { left: 32px;  width: 336px; }
  .panel--side-a { left: 400px; width: 188px; }
  .panel--front  { left: 620px; width: 328px; }
  .panel--side-b { left: 985px; width: 184px; }

  .turned {
    position: absolute;
    left: 50%;
    top: 50%;
    width: 130px;
    transform: translate(-50%, -50%) rotate(90deg);
    box-sizing: border-box;
    display: flex;
    flex-direction: column;
    align-items: center;
  }

  .brand {
    display: flex;
    align-items: center;
    gap: 5px;
  }
  .brand__mark {
    width: 30px;
    height: 30px;
    border: 1px solid var(--cream);
    box-sizing: border-box;
    flex: none;
  }
  .brand__name {
    font-family: "Kaushan Script", "Brush Script MT", "Segoe Script", cursive;
    color: var(--cream);
    font-size: 11px;
    line-height: 1.25;
  }

  .flavour {
    font-family: "Kaushan Script", "Brush Script MT", "Segoe Script", cursive;
    color: var(--title-gold);
    margin: 0;
    font-weight: 400;
    text-align: center;
    white-space: nowrap;
  }

  .panel--back .turned { height: 336px; padding: 10px 8px; justify-content: flex-start; }
  .panel--back .brand { margin-bottom: 10px; }
  .story {
    font-family: "Montserrat", sans-serif;
    font-size: 6.5px;
    line-height: 8.6px;
    color: var(--cream);
    text-align: justify;
    margin: 0;
  }

  .panel--side-a .turned { height: 188px; padding-top: 22px; gap: 24px; }
  .panel--side-b .turned { height: 184px; padding-top: 12px; gap: 22px; flex-direction: column-reverse; justify-content: flex-end; }
  .panel--side-b .turned { padding-top: 0; padding-bottom: 0; }
  .panel--side-a .flavour,
  .panel--side-b .flavour { font-size: 17px; line-height: 19px; }

  .panel--front .brand {
    position: absolute;
    top: 22px;
    left: 50%;
    transform: translateX(-50%);
  }
  .panel--front .brand__mark { width: 36px; height: 36px; }
  .panel--front .brand__name { font-size: 12px; }
  .panel--front .flavour {
    position: absolute;
    left: 0;
    right: 0;
    top: 74px;
    font-size: 27px;
    line-height: 32px;
  }
</style>
</head>
<body>
<div class="sleeve">

  <section class="panel panel--back">
    <div class="turned">
      <div class="brand">
        <span class="brand__mark"></span>
        <span class="brand__name">Nell's<br>Confections</span>
      </div>
      <p class="story">Lorem ipsum dolor sit amet, consectetur adipiscing elit, sed do eiusmod tempor incididunt ut labore et dolore magna aliqua. Ut enim ad minim veniam, quis nostrud exercitation ullamco laboris nisi ut aliquip ex ea commodo consequat. Duis aute irure dolor in reprehenderit in voluptate velit esse cillum dolore eu fugiat nulla pariatur. Excepteur sint occaecat cupidatat non proident, sunt in culpa qui officia deserunt mollit anim id est laborum. Sed ut perspiciatis unde omnis iste natus error sit voluptatem accusantium doloremque laudantium, totam rem aperiam eaque ipsa quae ab illo inventore veritatis. Nam libero tempore cum soluta nobis est eligendi optio cumque nihil impedit quo minus id quod maxime placeat facere possimus, omnis voluptas assumenda est. Temporibus autem quibusdam et aut officiis debitis rerum necessitatibus saepe eveniet ut et voluptates.</p>
    </div>
  </section>

  <section class="panel panel--side-a">
    <div class="turned">
      <div class="brand">
        <span class="brand__mark"></span>
        <span class="brand__name">Nell's<br>Confections</span>
      </div>
      <h2 class="flavour">Rosewater<br>&amp; Strawberry</h2>
    </div>
  </section>

  <section class="panel panel--front">
    <div class="brand">
      <span class="brand__mark"></span>
      <span class="brand__name">Nell's<br>Confections</span>
    </div>
    <h1 class="flavour">Rosewater &amp; Strawberry</h1>
  </section>

  <section class="panel panel--side-b">
    <div class="turned">
      <h2 class="flavour">Rosewater<br>&amp; Strawberry</h2>
      <div class="brand">
        <span class="brand__mark"></span>
        <span class="brand__name">Nell's<br>Confections</span>
      </div>
    </div>
  </section>

</div>
</body>
</html>
```